Digital content business needs banner ads

We sell content - if you need an article to put on your website or in a newsletter, you can purchase a ready made article from us and edit it to your liking to use straight away. This could be any kind of article, but this banner ad will be aimed at real estate agents. You can see the website (and the style of articles) here https://www.thebluelanternpost.com.au
The banner is meant to solve the problem of the front desk admin or agent trying to think of something to write to put in their email newsletter. This will save them time as they can just select an article from our library and use it (for a fee of course!).
Needs to have the words:
--------------------------------------------------
Find the next article for your newsletter
---------------------------------------------------
Some imagery would be good rather than plain text.
With a call to action like click here button or similar
Required sizes (or provide a set of standard sized ads):
728 x 90
970 x 250
300x250
Real Estate Agents

```html
<!DOCTYPE html>
<html lang="en">
<head>
<meta charset="utf-8">
<title>The Blue Lantern Post – Newsletter Article Banners</title>
<link href="https://fonts.googleapis.com/css2?family=Roboto+Condensed:wght@700&display=swap" rel="stylesheet">
<style>
  :root {
    --page: #ffffff;
    --ink: #111111;
    --red: #e0161b;
    --white: #ffffff;
    --blue: #0a9be0;
    --blue-deep: #0a7fc6;
    --navy: #0b4f95;
    --navy-dark: #083a72;
    --logo-blue: #2f78c4;
    --paper: #e3e6ea;
    --cloud-a: #f4e9ee;
    --cloud-b: #eef1f5;
  }
  html, body {
    margin: 0;
    width: 1200px;
    height: 637px;
    overflow: hidden;
    background: var(--page);
    font-family: "Roboto Condensed", "Arial Narrow", sans-serif;
    font-weight: 700;
  }
  .canvas { position: relative; width: 1200px; height: 637px; }

  .banner {
    position: absolute;
    height: 91px;
    border: 2px solid var(--ink);
    border-radius: 2px;
    overflow: hidden;
    box-sizing: border-box;
  }
  .banner--leaderboard { left: 240px; top: 117px; width: 708px; }
  .banner--billboard { left: 123px; top: 240px; width: 943px; }

  .word-cloud {
    position: absolute; inset: 0;
    background: linear-gradient(100deg, var(--cloud-a) 0%, var(--cloud-b) 45%, #f1eef2 80%);
  }
  .blue-field {
    position: absolute; inset: 0;
    background: linear-gradient(90deg, var(--blue) 0%, var(--blue-deep) 100%);
  }

  .panel { position: absolute; top: 0; height: 100%; }
  .article-photo {
    position: absolute;
    background: linear-gradient(90deg, #f4f4f4 0%, #8a8f96 55%, #3d434b 100%);
  }

  .headline {
    position: absolute;
    z-index: 2;
    margin: 0;
    line-height: 1;
    font-weight: 700;
    text-transform: uppercase;
    white-space: nowrap;
  }
  .headline__question, .headline__call { display: block; }

  .banner--leaderboard .headline { left: 21px; top: 15px; }
  .banner--leaderboard .headline__question { color: var(--red); font-size: 30px; }
  .banner--leaderboard .headline__call { color: var(--ink); font-size: 20.3px; margin-top: 3px; }

  .banner--billboard .headline { left: 19px; top: 8px; }
  .banner--billboard .headline__question { color: var(--white); font-size: 40.5px; }
  .banner--billboard .headline__call { color: var(--white); font-size: 27.5px; margin-top: 5px; }

  .brand {
    position: absolute;
    z-index: 2;
    display: flex;
    align-items: center;
    gap: 7px;
  }
  .brand__mark { width: 14px; height: 14px; background: var(--logo-blue); flex: none; }
  .brand__name {
    color: var(--ink);
    font-size: 16px;
    font-weight: 700;
    line-height: 1.05;
    text-transform: uppercase;
    white-space: nowrap;
  }
  .cta {
    position: absolute;
    z-index: 2;
    display: flex; align-items: center; justify-content: center;
    height: 21px;
    box-sizing: border-box;
    border-radius: 8px;
    background: linear-gradient(180deg, var(--navy) 0%, var(--navy-dark) 100%);
    color: var(--white);
    font-size: 13px;
    font-weight: 700;
    text-transform: uppercase;
    text-decoration: none;
    border: 1.5px solid var(--white);
  }
</style>
</head>
<body>
<main class="canvas">

  <section class="banner banner--leaderboard" aria-label="728 by 90 banner">
    <div class="word-cloud" role="img" aria-label="Faint word cloud of communication and language words"></div>
    <svg class="panel" style="left:360px;width:344px" viewBox="0 0 344 87" preserveAspectRatio="none" aria-hidden="true">
      <polygon points="30,0 344,0 344,87 0,87" fill="var(--paper)"/>
      <polygon points="200,0 344,0 344,87 172,87" fill="var(--white)"/>
    </svg>
    <div class="article-photo" role="img" aria-label="Newsletter page with a photo of a businessman in a suit"
         style="left:372px;top:0;width:170px;height:87px;clip-path:polygon(16% 0,100% 0,84% 100%,0 100%)"></div>
    <h1 class="headline">
      <span class="headline__question">Needs to have the words?</span>
      <span class="headline__call">Find the next article for your newsletter</span>
    </h1>
    <div class="brand" style="left:560px;top:18px">
      <span class="brand__mark"></span>
      <span class="brand__name">Blue Lantern<br>Post</span>
    </div>
    <a class="cta" href="https://www.thebluelanternpost.com.au" style="left:566px;top:63px;width:99px">Click here</a>
  </section>

  <section class="banner banner--billboard" aria-label="970 by 90 banner">
    <div class="blue-field"></div>
    <svg class="panel" style="left:563px;width:376px" viewBox="0 0 376 87" preserveAspectRatio="none" aria-hidden="true">
      <path d="M0 0 H376 C363 40 353 70 343 87 H30 C18 60 8 30 0 0 Z" fill="var(--paper)"/>
    </svg>
    <div class="article-photo" role="img" aria-label="Newsletter page with a photo of a businessman in a suit"
         style="left:600px;top:0;width:162px;height:87px;clip-path:polygon(18% 0,100% 0,82% 100%,0 100%)"></div>
    <h1 class="headline">
      <span class="headline__question">Needs to have the words?</span>
      <span class="headline__call">Find the next article for your newsletter</span>
    </h1>
    <div class="brand" style="left:784px;top:18px">
      <span class="brand__mark"></span>
      <span class="brand__name">Blue Lantern<br>Post</span>
    </div>
    <a class="cta" href="https://www.thebluelanternpost.com.au" style="left:790px;top:63px;width:99px">Click here</a>
  </section>

</main>
</body>
</html>
```